Enlargement project

We would like to create an enlargement of the attached business card design, so that we are able to print hi-res business cards from it,

The end result we are after is an illustrator template that contains hi-res graphics and text that we can edit to insert people's names, job titles, phone and email details

The two colours used within the design are:

Pantone 350 (green)
Panton 484 (red)

The fonts used are;

Futura Medium
Futura Bk BT Italic

Industry/Entity Type

Business

```html
<!DOCTYPE html>
<html lang="en">
<head>
<meta charset="utf-8">
<title>Sentrel business cards</title>
<link rel="stylesheet" href="https://fonts.googleapis.com/css2?family=Jost:wght@400;500&display=swap">
<style>
  :root {
    --page-bg: #e6e6e4;
    --card-bg: #ffffff;
    --brand-green: #2c5234;
    --brand-red: #9a3324;
    --brand-blue: #00a0dc;
    --accent-lime: #b5c938;
    --on-band: #ffffff;
  }
  * { margin: 0; padding: 0; box-sizing: border-box; }
  html, body { width: 1200px; height: 848px; overflow: hidden; }
  body {
    background: var(--page-bg);
    font-family: "Jost", "Futura", sans-serif;
    font-weight: 500;
  }
  .canvas {
    position: relative;
    width: 1200px;
    height: 848px;
  }
  .card {
    position: absolute;
    left: 320px;
    width: 560px;
    height: 340px;
    background: var(--card-bg);
    box-shadow: 0 2px 10px rgba(0,0,0,0.18);
    overflow: hidden;
  }
  .card--classic { top: 64px; --ink: var(--brand-green); --accent: var(--brand-red); }
  .card--fresh { top: 444px; --ink: var(--brand-blue); --accent: var(--brand-blue); }

  .wordmark {
    position: absolute;
    left: 30px;
    top: 50px;
    display: flex;
    align-items: center;
    gap: 10px;
  }
  .wordmark-name {
    font-size: 38px;
    line-height: 1;
    color: var(--ink);
    font-weight: 500;
  }
  .wordmark-square {
    width: 56px;
    height: 56px;
    background: var(--accent);
  }

  .address, .numbers, .email {
    position: absolute;
    left: 30px;
    color: var(--ink);
    font-size: 14.5px;
    line-height: 19px;
  }
  .address { top: 148px; }
  .numbers { top: 222px; }
  .email { top: 288px; }
  .website {
    position: absolute;
    right: 30px;
    top: 288px;
    color: var(--ink);
    font-size: 14.5px;
    line-height: 19px;
  }

  .person {
    position: absolute;
    left: 378px;
    top: 146px;
    color: var(--brand-red);
  }
  .person-name { font-size: 22px; line-height: 26px; font-weight: 400; }
  .person-role { font-size: 13.5px; line-height: 18px; }

  .name-band {
    position: absolute;
    left: 316px;
    top: 140px;
    width: 244px;
    height: 72px;
  }
  .card--fresh .person {
    left: 378px;
    top: 150px;
    color: var(--on-band);
  }
  .swoop {
    position: absolute;
    left: 0;
    top: 0;
    width: 560px;
    height: 340px;
  }
</style>
</head>
<body>
<main class="canvas">

  <section class="card card--classic" aria-label="Business card, green and red edition">
    <div class="wordmark">
      <span class="wordmark-name">Sentrel</span>
      <span class="wordmark-square" aria-hidden="true"></span>
    </div>
    <div class="person">
      <p class="person-name">Dana Whitlow</p>
      <p class="person-role">Technical Operations</p>
    </div>
    <address class="address" style="font-style:normal">
      Suite 4, Level 2<br>
      88 Harbour Lane<br>
      Sydney NSW 2000
    </address>
    <p class="numbers">
      t.&nbsp; 02 7100 0000<br>
      f.&nbsp; 02 7100 1111<br>
      d.&nbsp;02 7100 2222
    </p>
    <p class="email">dwhitlow@sentrel.net</p>
    <p class="website">www.sentrel.net</p>
  </section>

  <section class="card card--fresh" aria-label="Business card, blue edition">
    <svg class="swoop" viewBox="0 0 560 340" aria-hidden="true">
      <path d="M340 340 Q 410 220 560 206" fill="none" stroke="var(--accent-lime)" stroke-width="4"/>
    </svg>
    <svg class="name-band" viewBox="0 0 244 72" aria-hidden="true">
      <polygon points="0,0 244,0 244,60 16,72" fill="var(--brand-blue)"/>
    </svg>
    <div class="wordmark">
      <span class="wordmark-name">Sentrel</span>
      <span class="wordmark-square" aria-hidden="true"></span>
    </div>
    <div class="person">
      <p class="person-name">Dana Whitlow</p>
      <p class="person-role">Technical Operations</p>
    </div>
    <address class="address" style="font-style:normal">
      Suite 4, Level 2<br>
      88 Harbour Lane<br>
      Sydney NSW 2000
    </address>
    <p class="numbers">
      t.&nbsp; 02 7100 0000<br>
      f.&nbsp; 02 7100 1111<br>
      d.&nbsp;02 7100 2222
    </p>
    <p class="email">dwhitlow@sentrel.net</p>
    <p class="website">www.sentrel.net</p>
  </section>

</main>
</body>
</html>
```